Calderon Lending. Website design for a mortgage company.

We need a simple, but classy and artistic website design. The website should contain a home page, about page, and information page. I would like the design for each page created and I can add the content.

Calderon Lending is a retail mortgage broker business specially crafted to provide simple, transparent, and comprehensive mortgage solutions. We understand the complexities of mortgage acquisition and have aligned with the best partners and resources to analyze the information and deliver precise, transparent, efficient, and reliable results.

Target Market(s)

We are targeting people ages 30-65 within the United States, both male and female. We are also targeting business owners and property investors specifically.

Industry/Entity Type

Mortgage Brokerage

Coding

Coded - Design and coding required

Number of Pages Required

5+ page

Font styles to use
Sans Serif
Script

Requirements
Must have
• The main purpose of this website is to provide clients with the necessary information to want to move forward with a loan transaction. The website will be informational to promote the company and showcase our purpose. The company purpose is to provide efficient and comprehensive service to clients, and to help them navigate the challenging mortgage world.

The website must mimic that of the major fortune 500 companies. It needs to be super clean, but very modern. The pictures should be of families with brown skin mostly.

The website needs to be mobile responsive. Each page needs to consist of large and responsive Hero Images. There will be background videos on the product and process pages of the website.

The website must have a semi-flat design.
The website must have a Hamburger Menu instead of a visible navigation menu.

Use the script font styles for the headlines and the sans serif for body text.

We need to have the following pages:
Home

Products

Process

About

Contact - I want a map of our office location and region. We are located in Bowie MD and our region consists of the following states: Florida, Texas, Virginia, Maryland, and Washington DC.

```html
<!DOCTYPE html>
<html lang="en">
<head>
<meta charset="utf-8">
<title>Calderon Lending</title>
<link rel="stylesheet" href="https://fonts.googleapis.com/css2?family=Roboto:wght@400;500;700&family=Lobster&family=Marck+Script&display=swap">
<style>
:root{
  --frame:#000000;
  --blue:#338dbb;
  --blue-text:#3a8fc0;
  --beige:#e2d8d3;
  --mist:#e9ecf3;
  --dark:#373737;
  --ink:#222222;
  --muted:#8a8a8a;
  --footer:#2d2d2d;
  --white:#ffffff;
  --green:#5cc17b;
  --bar-blue:#2a9be0;
  --bar-light:#9fd3f5;
}
*{margin:0;padding:0;box-sizing:border-box}
html,body{width:1200px;height:2321px;overflow:hidden}
body{background:var(--frame);font-family:"Roboto",Arial,sans-serif;color:var(--ink);position:relative}
.page{position:absolute;left:67px;top:67px;width:1066px;height:2187px;background:var(--white);overflow:hidden}
.abs{position:absolute}

/* hero */
.hero{left:0;top:0;width:1066px;height:771px;
  background:linear-gradient(180deg,#c9e4ec 0%,#bcdcda 35%,#b59a6e 52%,#9cbf55 72%,#6f9a2a 100%)}
.logo{left:209px;top:0;width:112px;height:118px;background:var(--white);text-align:center;padding-top:41px;box-shadow:0 2px 4px rgba(0,0,0,.12)}
.logo-name{font-size:19px;font-weight:500;letter-spacing:.5px;line-height:20px}
.logo-sub{font-size:14px;line-height:18px;letter-spacing:.5px}
.menu-btn{left:824px;top:29px;width:34px;height:32px;background:var(--white);border-radius:2px}
.menu-btn span{position:absolute;left:8px;width:19px;height:2px;background:#222}
.hero-title{left:220px;top:160px;font-family:"Marck Script",cursive;font-size:41px;line-height:45px;color:var(--blue-text)}
.hero-lead{left:227px;top:300px;font-size:14.5px;line-height:22px;color:#1c1c1c}
.btn{left:228px;top:358px;width:104px;height:24px;border-radius:12px;background:var(--blue);color:var(--white);font-size:8.5px;font-weight:500;text-align:center;line-height:24px;letter-spacing:.3px}
.why{left:512px;top:539px;width:269px;height:147px;background:var(--white);text-align:center;box-shadow:0 3px 8px rgba(0,0,0,.15)}
.why-plus{left:557px;top:529px;width:28px;height:28px;border-radius:50%;background:#f2b447;border:3px solid #e9eef2;color:#5a3a00;font-size:16px;text-align:center;line-height:22px}
.why h3{font-family:"Lobster",cursive;font-weight:400;font-size:22px;color:var(--blue);margin-top:32px}
.why p{font-size:10px;line-height:15px;margin:10px 22px 0;color:#222}

/* opportunity */
.opportunity{left:0;top:771px;width:1066px;height:380px;background:var(--beige)}
.section-title{left:0;width:1066px;text-align:center;font-family:"Lobster",cursive;font-weight:400;font-size:33px;color:var(--ink)}
.market{left:206px;top:129px;width:319px;height:183px;background:var(--white)}
.donut{left:10px;top:33px}
.donut-label{left:10px;top:76px;width:120px;text-align:center}
.donut-value{font-size:26px;font-weight:500;line-height:28px;color:#333}
.donut-sub{font-size:12.5px;color:#555}
.market h3{position:absolute;left:139px;top:31px;font-size:18.5px;font-weight:500}
.legend{left:139px;top:69px;list-style:none;font-size:10.5px;line-height:16.3px;color:var(--muted)}
.legend i{display:inline-block;width:8px;height:8px;margin-right:3px;border-radius:1px}
.problems{left:548px;top:129px;width:311px;height:183px;background:var(--blue);color:var(--white);padding:18px 0 0 20px}
.card-title{font-size:19px;font-weight:500;margin-bottom:12px}
.problems ol{list-style:none;font-size:13px;line-height:23.4px}

/* solution */
.solution{left:0;top:1151px;width:1066px;height:303px;background:var(--mist)}
.our-solution{left:207px;top:52px;width:286px;height:194px;background:var(--blue);color:var(--white);padding:18px 20px 0 20px}
.our-solution p{font-size:13px;line-height:20.3px}
.compare{left:503px;top:52px;width:355px;border-collapse:collapse;background:var(--white);font-size:9.5px}
.compare th{background:#333;color:var(--white);height:38px;text-align:left;padding-left:14px;font-weight:500;font-size:8.5px}
.compare td{height:31.5px;padding-left:14px;border-bottom:1px solid #ececec;color:#333}
.compare th:first-child,.compare td:first-child{width:127px;border-right:1px solid #ddd}

/* sales */
.sales{left:0;top:1454px;width:1066px;height:688px;background:linear-gradient(180deg,#eef2f6 0%,#ffffff 14%)}
.house-art{left:14px;top:65px;width:459px;height:252px;border-radius:40%;background:radial-gradient(ellipse at 50% 50%,#c8b49a 0%,#a9c27a 40%,#e3ecec 70%,rgba(255,255,255,0) 100%)}
.channels{left:471px;top:105px;width:270px;height:247px;background:var(--dark);color:var(--white);padding:24px 18px 0}
.channels ol{list-style:none;font-size:12.3px;line-height:24.3px;color:#dedede;margin-top:16px}
.activities{left:755px;top:105px;width:270px;height:247px;background:var(--mist);padding:24px 19px 0}
.activities p{font-size:13.3px;line-height:20px;color:#444;margin-top:14px}

.fin-card{top:470px;width:208px;height:176px;background:var(--white);box-shadow:0 0 0 1px #ececec,0 2px 6px rgba(0,0,0,.08)}
.fin-card svg text{font-family:"Roboto",Arial,sans-serif}

/* footer */
.footer{left:0;top:2143px;width:1066px;height:44px;background:var(--footer);color:#cfcfcf;font-size:8.5px}
.footer .copy{position:absolute;left:207px;top:17px}
.footer .links{position:absolute;right:208px;top:17px}
.footer .links span{margin:0 10px}
.footer .links u{color:#e6e6e6}
</style>
</head>
<body>
<main class="page">

  <section class="hero abs" role="img" aria-label="Photo of a family playing football on a sunny meadow in front of a log house with pine trees and a hawk overhead"></section>
  <div class="logo abs"><div class="logo-name">CALDERON</div><div class="logo-sub">LENDING</div></div>
  <div class="menu-btn abs"><span style="top:9px"></span><span style="top:15px"></span><span style="top:21px"></span></div>
  <h1 class="hero-title abs" style="font-weight:400">Big Dreams<br>Even Bigger and<br>Better Loans</h1>
  <p class="hero-lead abs">An intelligent way to make your<br>dreams come true!</p>
  <div class="btn abs">PRODUCTS</div>
  <div class="why abs">
    <h3>Why Calderon Lending</h3>
    <p>Calderon Lending is a retail mortgage broker business specially crafted to provide simple, transparent, and comprehensive mortgage solutions.</p>
  </div>
  <div class="why-plus abs">+</div>

  <section class="opportunity abs">
    <h2 class="section-title abs" style="top:36px">Our Opportunity</h2>
    <div class="market abs">
      <svg class="donut abs" width="120" height="120" viewBox="0 0 120 120">
        <g transform="rotate(-90 60 60)" fill="none" stroke-width="17">
          <circle cx="60" cy="60" r="50" stroke="#4fb6e6" stroke-dasharray="128.8 314.2" stroke-dashoffset="0"/>
          <circle cx="60" cy="60" r="50" stroke="#f5c542" stroke-dasharray="106.8 314.2" stroke-dashoffset="-128.8"/>
          <circle cx="60" cy="60" r="50" stroke="#8cc63f" stroke-dasharray="47.1 314.2" stroke-dashoffset="-235.6"/>
          <circle cx="60" cy="60" r="50" stroke="#f09a2a" stroke-dasharray="28.3 314.2" stroke-dashoffset="-282.7"/>
          <circle cx="60" cy="60" r="50" stroke="#9b8fe0" stroke-dasharray="3.2 314.2" stroke-dashoffset="-311"/>
        </g>
      </svg>
      <div class="donut-label abs"><div class="donut-value">867K</div><div class="donut-sub">Prospects</div></div>
      <h3>Target market</h3>
      <ul class="legend abs">
        <li><i style="background:#4fb6e6"></i>Texas&nbsp;&nbsp; 41% ($85.7B)</li>
        <li><i style="background:#f5c542"></i>Florida&nbsp;&nbsp; 34% ($77.6B)</li>
        <li><i style="background:#8cc63f"></i>Virginia&nbsp;&nbsp; 15% ($37.3B)</li>
        <li><i style="background:#f09a2a"></i>Maryland&nbsp;&nbsp; 9% ($24.3B)</li>
        <li><i style="background:#9b8fe0"></i>District of Columbia&nbsp;&nbsp; 1% ($5.2B)</li>
      </ul>
    </div>
    <div class="problems abs">
      <h3 class="card-title">Problems worth solving</h3>
      <ol>
        <li>1. Understanding complex mortgage terms.</li>
        <li>2. Lack of transparent communication.</li>
        <li>3. Improper expectation setting.</li>
        <li>4. Getting quick and reliable results.</li>
        <li>5. Shopping for the best mortgage rates.</li>
      </ol>
    </div>
  </section>

  <section class="solution abs">
    <div class="our-solution abs">
      <h3 class="card-title">Our solution</h3>
      <p>We understand the complexities of mortgage acquisition and have aligned with the best partners and resources to analyze the information and deliver precise, transparent, efficient, and reliable results.</p>
    </div>
    <table class="compare abs">
      <thead><tr><th>COMPETITORS</th><th>HOW OUR SOLUTION IS BETTER</th></tr></thead>
      <tbody>
        <tr><td>Steadfast Rate</td><td>Higher service level</td></tr>
        <tr><td>Pine Hollow Mortgage</td><td>More broad loan selection</td></tr>
        <tr><td>Loan Works</td><td>Customized process approach</td></tr>
        <tr><td>Orion Home Loans</td><td>Transparent workflow</td></tr>
        <tr><td>Brightloan.com</td><td>Greater flexibility</td></tr>
      </tbody>
    </table>
  </section>

  <section class="sales abs">
    <h2 class="section-title abs" style="top:40px">Sales and Marketing</h2>
    <div class="house-art abs" role="img" aria-label="Illustration of a cutaway two-storey house on a grassy island with numbered hotspots"></div>
    <div class="channels abs">
      <h3 class="card-title" style="font-size:20px">Sales Channels</h3>
      <ol>
        <li>1. Effective Search Engine Optimization SEO</li>
        <li>2. Digital training solutions</li>
        <li>3. Interactive online webinars</li>
        <li>4. Strategic partnerships</li>
        <li>5. Group networking seminars</li>
      </ol>
    </div>
    <div class="activities abs">
      <h3 class="card-title" style="font-size:20px;color:var(--ink);margin:0">Marketing Activities</h3>
      <p>Utilizing effective search engine optimization, we will position our website to be visible to consumers seeking specific loan products. Aligning with innovative partners, we will expose ourselves to prospects during in-person and digital training.</p>
    </div>

    <h2 class="section-title abs" style="top:400px">Financial Projections</h2>

    <div class="fin-card abs" style="left:207px">
      <svg width="208" height="176" viewBox="0 0 208 176" font-size="7.5" font-weight="700" fill="#222" text-anchor="middle">
        <rect x="19" y="99" width="18" height="15" fill="var(--bar-blue)"/>
        <rect x="57" y="35" width="18" height="79" fill="var(--bar-blue)"/>
        <rect x="95" y="23" width="18" height="91" fill="var(--bar-blue)"/>
        <line x1="10" y1="114" x2="198" y2="114" stroke="#bbb" stroke-width="2"/>
        <text x="28" y="95">$162K</text><text x="66" y="31">$811K</text><text x="104" y="19">$932K</text>
        <text x="141" y="110">$0</text><text x="179" y="110">$0</text>
        <g font-size="9.5"><text x="28" y="131">FY'21</text><text x="66" y="131">FY'22</text><text x="104" y="131">FY'23</text><text x="141" y="131">FY'24</text><text x="179" y="131">FY'25</text></g>
        <text x="104" y="153" font-size="13">Revenue</text>
      </svg>
    </div>

    <div class="fin-card abs" style="left:432px">
      <svg width="208" height="176" viewBox="0 0 208 176" font-size="7.5" font-weight="700" fill="#222" text-anchor="middle">
        <rect x="18" y="85" width="18" height="7" fill="var(--bar-light)" stroke="#5ab4ea"/>
        <rect x="56" y="62" width="18" height="30" fill="var(--bar-light)" stroke="#5ab4ea"/>
        <rect x="94" y="58" width="18" height="34" fill="var(--bar-light)" stroke="#5ab4ea"/>
        <line x1="8" y1="92" x2="198" y2="92" stroke="#888" stroke-width="2"/>
        <text x="27" y="81">$69K</text><text x="65" y="58">$303K</text><text x="103" y="54">$347K</text>
        <text x="141" y="88">$10K</text><text x="180" y="88">$10K</text>
        <g font-size="9.5"><text x="27" y="108">FY'21</text><text x="65" y="108">FY'22</text><text x="103" y="108">FY'23</text><text x="141" y="108">FY'24</text><text x="180" y="108">FY'25</text></g>
        <text x="104" y="129" font-size="13" letter-spacing=".5">Expenses &amp; Costs</text>
      </svg>
    </div>

    <div class="fin-card abs" style="left:658px">
      <svg width="208" height="176" viewBox="0 0 208 176" font-size="7.5" font-weight="700" fill="#222" text-anchor="middle">
        <rect x="20" y="59" width="18" height="4" fill="var(--green)"/>
        <rect x="58" y="39" width="18" height="24" fill="var(--green)"/>
        <rect x="95" y="36" width="18" height="27" fill="var(--green)"/>
        <rect x="133" y="63" width="18" height="2" fill="#aaa"/>
        <rect x="170" y="63" width="18" height="2" fill="#aaa"/>
        <line x1="10" y1="63" x2="198" y2="63" stroke="#bbb" stroke-width="1.5"/>
        <text x="29" y="55">$93K</text><text x="67" y="35">$508K</text><text x="104" y="32">$586K</text>
        <text x="142" y="76">($10K)</text><text x="179" y="76">($10K)</text>
        <g font-size="9.5"><text x="29" y="127">FY'21</text><text x="67" y="127">FY'22</text><text x="104" y="127">FY'23</text><text x="142" y="127">FY'24</text><text x="179" y="127">FY'25</text></g>
        <text x="104" y="148" font-size="13">Profit</text>
      </svg>
    </div>
  </section>

  <footer class="footer abs">
    <span class="copy">© Copyright 2020 All Right Reserved.</span>
    <span class="links"><u>Privacy Statement</u><span>|</span>Terms Of Use</span>
  </footer>

</main>
</body>
</html>
```